letter head for a construction company

Company Name: Zaviro Construction Limited

Address: Kilele Street, Tengeru Shores, Dar es salaam, Tanzania

Phone: 0754382916

email : info@zaviroconstruction.example

website : www.zaviroconstruction.example

```html
<!DOCTYPE html>
<html lang="en">
<head>
<meta charset="utf-8">
<title>Zaviro Construction Limited — Letterhead</title>
<link rel="stylesheet" href="https://fonts.googleapis.com/css2?family=Montserrat:wght@600&family=Inter:wght@300;400;600&display=swap">
<style>
  :root {
    --backdrop: #e9eaec;
    --paper: #ffffff;
    --ink: #3a3a3c;
    --ink-soft: #4a4a4d;
    --accent: #f47b06;
    --band-dark: #48484b;
  }
  * { margin: 0; padding: 0; box-sizing: border-box; }
  html, body {
    width: 1200px; height: 1179px; overflow: hidden;
    background: var(--backdrop);
  }
  .letterhead {
    position: absolute; left: 182px; top: 0;
    width: 836px; height: 1179px;
    background: var(--paper);
    font-family: "Inter", Arial, sans-serif;
    color: var(--ink);
  }
  .brand {
    position: absolute; left: 72px; top: 84px;
    font-family: "Montserrat", Arial, sans-serif;
    font-weight: 600; color: var(--ink);
  }
  .brand-name { font-size: 40px; line-height: 40px; letter-spacing: 0.5px; }
  .brand-sub { font-size: 13.5px; letter-spacing: 5.2px; margin-top: 4px; }
  .contact {
    position: absolute; left: 581px; top: 88px;
    font-size: 10.8px; line-height: 14.5px; color: var(--ink);
  }
  .contact-group { border-left: 2px solid var(--accent); padding-left: 10px; }
  .contact-group.lines { border-left: 1px solid var(--ink-soft); margin-top: 10px; padding: 1px 0 2px 10px; }
  .contact-row { display: flex; align-items: center; gap: 5px; }
  .contact-row svg { width: 10px; height: 10px; flex: none; }
  .recipient {
    position: absolute; left: 77px; top: 340px;
    font-size: 12.4px; line-height: 15px; font-weight: 300;
  }
  .letter-body {
    position: absolute; left: 77px; top: 464px; width: 686px;
    font-size: 12.1px; line-height: 14.9px; font-weight: 300;
    letter-spacing: -0.15px;
  }
  .salutation { font-weight: 600; margin-bottom: 15px; }
  .letter-body p { text-align: justify; margin-bottom: 14.9px; }
  .closing { position: absolute; left: 77px; top: 842px; font-size: 12.1px; font-weight: 300; }
  .signature { position: absolute; left: 73px; top: 868px; width: 140px; height: 60px; }
  .signatory { position: absolute; left: 77px; top: 946px; font-size: 12.4px; line-height: 15px; }
  .signatory strong { font-weight: 600; display: block; }
  .signatory span { font-weight: 300; }
  .footer-band { position: absolute; left: 0; bottom: 0; width: 836px; height: 19px; }
</style>
</head>
<body>
<main class="letterhead">
  <header>
    <div class="brand">
      <div class="brand-name">ZAVIRO</div>
      <div class="brand-sub">CONSTRUCTION LTD</div>
    </div>
    <address class="contact" style="font-style:normal">
      <div class="contact-group">
        Kilele Street, Tengeru Shores,<br>Dar es salaam, Tanzania
      </div>
      <div class="contact-group lines">
        <div class="contact-row">
          <svg viewBox="0 0 10 10"><path d="M2 1 L3.6 1 L4.2 3 L3.2 3.8 Q4 5.8 6 6.8 L6.9 5.8 L9 6.4 L9 8 Q8.5 9 7.5 9 Q1 8 1 2 Q1 1 2 1Z" fill="var(--accent)"/></svg>
          0754382916
        </div>
        <div class="contact-row">
          <svg viewBox="0 0 10 10"><rect x="0.5" y="2" width="9" height="6" fill="var(--accent)"/><path d="M0.5 2 L5 5.5 L9.5 2" stroke="#fff" stroke-width="1" fill="none"/></svg>
          info@zaviroconstruction.example
        </div>
        <div class="contact-row">
          <svg viewBox="0 0 10 10" fill="none" stroke="var(--accent)" stroke-width="0.9"><circle cx="5" cy="5" r="4.2"/><ellipse cx="5" cy="5" rx="1.8" ry="4.2"/><path d="M0.8 5 H9.2 M1.6 2.8 H8.4 M1.6 7.2 H8.4"/></svg>
          www.zaviroconstruction.example
        </div>
      </div>
    </address>
  </header>

  <div class="recipient">
    Mr. Marcus Delworth<br>President and CEO<br>Veritane Labs LLC.<br>2210 Harlow Avenue, Suite 310<br>New York, NY 10099
  </div>

  <section class="letter-body">
    <div class="salutation">Dear Mr. Delworth:</div>
    <p>As Chairperson of the Corporate Conscience Campaign - Helping the Homeless in New York, I am writing this to thank you personally for your company's support in last month's fund-raising effort.</p>
    <p>As I indicated when we spoke on the phone two weeks ago, the campaign was considered a resounding success, raising a total of $1.65 million to-date, significantly exceeding our target of $1 million. Some donations are still trickling in, so we could end up close to a total of $2 million.</p>
    <p>Veritane Labs was an influential leader throughout the entire three-month campaign. In fact, we couldn't have succeeded without the generous support of your company, both financially, and through your organizational and administrative assistance. Your Team Leader, Renata Holloway was particularly impressive, going above and beyond what we could have expected of someone performing as a volunteer while continuing on with her day-to-day duties. Please convey my special thanks to Renata.</p>
    <p>I would also ask you to convey my sincere thanks and congratulations to all of those other people in your company who contributed in any way to the Helping the Homeless Campaign. Please tell them that the sum of their contributions resulted in a major success that they should all be proud of taking part in.</p>
    <p>I believe that the 27 companies that participated in this effort have set a new standard for social responsibility in this community, and have set a powerful example that will inspire other companies and organizations to do the same.</p>
    <p>I look forward to seeing you at the Mayor's special thank you reception next month.</p>
  </section>

  <div class="closing">Yours sincerely,</div>
  <svg class="signature" role="img" aria-label="Handwritten signature of the fundraising chair" viewBox="0 0 140 60">
    <rect width="140" height="60" rx="4" fill="#f1f1f2"/>
  </svg>
  <div class="signatory">
    <strong>Daniel Okoro</strong>
    <span>Fundraising Chair</span>
  </div>

  <svg class="footer-band" viewBox="0 0 836 19" preserveAspectRatio="none" aria-hidden="true">
    <polygon points="0,8 540,8 532,19 0,19" fill="var(--band-dark)"/>
    <polygon points="554,1 836,1 836,19 540,19" fill="var(--accent)"/>
  </svg>
</main>
</body>
</html>
```